New Business Card Design Project

Bloom of the Willow Wellness Clinic PLLC
Bloomofthewillowwc-example.com
Board Certified Nursing Coach in life, health, & wellness.
Hypnotherapy, weight loss & vitamin supplement injections, IV hydration.
Offering mobile clinics

```html
<!DOCTYPE html>
<html lang="en">
<head>
<meta charset="utf-8">
<title>Bloom of the Willow Wellness Clinic – Business Card</title>
<link href="https://fonts.googleapis.com/css2?family=Open+Sans:wght@400;700&display=swap" rel="stylesheet">
<style>
  :root {
    --stage: #ababab;
    --front-dark: #46352a;
    --front-glow: #5c463a;
    --back-light: #f7f9e7;
    --back-shade: #e9e9d6;
    --accent: #d4502a;
    --ink: #3a2e24;
    --body-ink: #4a3d33;
    --cream: #f6ecd0;
    --amber: #d98a3a;
  }
  * { box-sizing: border-box; margin: 0; padding: 0; }
  html, body {
    width: 1200px; height: 1000px; overflow: hidden;
    background: var(--stage);
    font-family: "Open Sans", Arial, sans-serif;
  }
  .card {
    position: absolute;
    left: 293px;
    width: 615px;
    height: 353px;
    border-radius: 16px;
    overflow: hidden;
    box-shadow: 0 10px 18px rgba(0,0,0,0.28);
  }
  .card-front {
    top: 147px;
    background: radial-gradient(ellipse 55% 60% at 50% 52%, var(--front-glow) 0%, var(--front-dark) 70%);
  }
  .front-mark {
    position: absolute;
    left: 50%; top: 74px;
    transform: translateX(-50%);
    width: 130px; height: 130px;
    border-radius: 50%;
    background: radial-gradient(circle at 50% 45%, #f3d9a4 0%, var(--amber) 60%, #8a4a22 100%);
    opacity: 0.85;
  }
  .front-name {
    position: absolute;
    left: 0; right: 0; top: 168px;
    text-align: center;
    color: var(--cream);
    font-weight: 700;
  }
  .front-name .title {
    display: block;
    font-size: 30px;
    letter-spacing: 3px;
    text-transform: uppercase;
  }
  .front-name .subtitle {
    display: block;
    margin-top: 14px;
    font-size: 15px;
    letter-spacing: 3px;
    text-transform: uppercase;
  }
  .card-back {
    top: 531px;
    background: linear-gradient(90deg, var(--back-light) 0%, var(--back-light) 45%, var(--back-shade) 100%);
  }
  .back-decor {
    position: absolute;
    right: -40px; top: 20px;
    width: 320px; height: 340px;
    border-radius: 50%;
    background: radial-gradient(circle, rgba(225,225,205,0.6) 0%, rgba(225,225,205,0) 70%);
  }
  .back-content {
    position: absolute;
    left: 60px; top: 50px;
  }
  .company {
    font-size: 23px;
    font-weight: 700;
    color: var(--accent);
    line-height: 29px;
  }
  .website {
    font-size: 23px;
    font-weight: 700;
    color: var(--ink);
    line-height: 29px;
  }
  .services {
    list-style: none;
    margin-top: 24px;
    width: 340px;
  }
  .services li {
    position: relative;
    padding-left: 15px;
    font-size: 18px;
    line-height: 22px;
    color: var(--body-ink);
    margin-bottom: 20px;
  }
  .services li::before {
    content: "";
    position: absolute;
    left: -2px; top: 9px;
    width: 7px; height: 7px;
    border-radius: 50%;
    background: var(--accent);
  }
</style>
</head>
<body>
  <section class="card card-front">
    <div class="front-mark"></div>
    <div class="front-name">
      <span class="title">Bloom of the Willow</span>
      <span class="subtitle">Wellness Clinic</span>
    </div>
  </section>

  <section class="card card-back">
    <div class="back-decor" role="img" aria-label="Faint brand emblem decoration"></div>
    <div class="back-content">
      <h1 class="company">Bloom of the Willow Wellness Clinic PLLC</h1>
      <p class="website">Bloomofthewillowwc-example.com</p>
      <ul class="services">
        <li>Board Certified Nursing Coach in life, health, &amp; wellness.</li>
        <li>Hypnotherapy, weight loss &amp; vitamin supplement injections, IV hydration.</li>
        <li>Offering mobile clinics</li>
      </ul>
    </div>
  </section>
</body>
</html>
```